Design Challege - Simplify a Complex Message

We have a new website design, but one of the pages presents a particular problem.

Our company does ERP implementations. We have developed a proprietary approach to these implementations based on the idea that you must get eight (and only eight) things right. These eight things are listed below, summarized in one or two words each:

1. Value
2. Capability
3. Functionality
4. Data
5. Technology
6. Change Leadership
7. Quality
8. Governance

Each of these eight things can be summarized in a short paragraph, but when you combine all eight summaries with a brief introductory text, the result is a lot of text - so much text that the casual surfer may be overwhelmed by it.

The winning design will find an engaging way to present the information in a way that presents a high-level summary, using icons and one- or two-word descriptions above but revealing more information when clicked.

Our current design for this information, with a paragraph describing the eight elements in a table, is included as an upload in PDF and Microsoft Word formats. We are looking for a creative way to display these eight things, showing the detail only when the user wants to see it.

The website is being built in WordPress, using Elementor as a page builder.

We will implement (code) the page, but the winner will be asked to specify the widget or other add-in if one is required.

The design does not need to include a header or footer, we have those.

Target Market(s)

Business executives working in technology

Industry/Entity Type

Any

Number of Pages Required

1 page

Font styles to use
Sans Serif

Requirements
Must have
• A design for the body of the page, but not the header or footer.
Nice to have
• Unique icons or images appropriate for each of the eight things.
Should not have
• A lot of text on one page

```html
<!DOCTYPE html>
<html lang="en">
<head>
<meta charset="utf-8">
<title>Eight Things to Get Right</title>
<link href="https://fonts.googleapis.com/css2?family=Open+Sans:wght@400;600&display=swap" rel="stylesheet">
<style>
  :root {
    --brand: #00b8de;
    --page: #f6fafc;
    --card: #ffffff;
    --ink: #111111;
    --muted: #8a8f94;
    --edge: #eef1f3;
  }
  * { margin: 0; padding: 0; box-sizing: border-box; }
  html, body { width: 1200px; height: 715px; overflow: hidden; }
  body {
    position: relative;
    background: var(--page);
    font-family: "Open Sans", Arial, sans-serif;
    color: var(--ink);
  }
  .backdrop { position: absolute; inset: 0; }
  .panel {
    position: absolute; left: 110px; top: 82px; width: 980px; height: 551px;
    background: var(--card); border-radius: 51px;
    box-shadow: 0 10px 40px rgba(0, 60, 90, 0.06);
  }
  .headline {
    position: absolute; left: 178px; top: 138px;
    font-size: 27.5px; font-weight: 600; line-height: 36px; white-space: nowrap;
  }
  .headline .accent { color: var(--brand); }
  .intro {
    position: absolute; left: 670px; top: 133px; width: 340px;
    font-size: 7.3px; line-height: 11.7px; color: var(--muted); white-space: nowrap;
  }
  .pillar { position: absolute; width: 200px; height: 170px; }
  .pillar .frame { position: absolute; left: 0; top: 0; }
  .pillar .badge { position: absolute; left: 0; top: 61px; width: 45px; height: 45px; }
  .pillar .copy { position: absolute; left: 51px; top: 29px; width: 130px; height: 92px; }
  .pillar h2 { font-size: 11px; font-weight: 400; line-height: 14px; margin-bottom: 6px; white-space: nowrap; }
  .pillar p { font-size: 7.3px; line-height: 11.5px; color: var(--muted); white-space: nowrap; }
  .pillar .more {
    position: absolute; left: 0; top: 80px;
    font-size: 7.8px; line-height: 10px; font-weight: 600; color: var(--brand); text-decoration: none;
  }
  .outro {
    position: absolute; left: 327px; top: 651px;
    font-size: 18.2px; line-height: 26px; color: var(--ink); white-space: nowrap;
  }
</style>
</head>
<body>
  <svg class="backdrop" width="1200" height="715" aria-hidden="true">
    <polygon points="938,0 1200,0 1200,258 1177,278 918,278 918,20" fill="var(--brand)"/>
    <polygon points="18,439 276,439 276,697 258,715 0,715 0,457" fill="var(--brand)"/>
  </svg>

  <div class="panel"></div>

  <h1 class="headline"><span class="accent">Eight Things</span> to Get Right</h1>
  <p class="intro">Like the roots and branches of a tree, there are many considerations in an ERP implementation.<br>Focus too much on the minor details, and you can lose sight of the tree.<br>In an ERP implementation, you must get eight major things right to be successful. Ignore any of<br>them, and your implementation will fail. Get them right, and you will likely succeed.</p>

  <svg width="0" height="0" style="position:absolute">
    <defs>
      <g id="pillar-frame">
        <polygon points="68,0 150,0 196,46 196,120 150,166 68,166 22,120 22,46" fill="#fff" stroke="var(--edge)" stroke-width="1"/>
        <polyline points="152,11 193,50 193,118 152,158" fill="none" stroke="var(--brand)" stroke-width="7" stroke-linejoin="miter"/>
      </g>
      <g id="badge-shape">
        <polygon points="13,0 32,0 45,13 45,32 32,45 13,45 0,32 0,13" fill="var(--brand)"/>
      </g>
    </defs>
  </svg>

  <!-- Row one -->
  <article class="pillar" style="left:182px;top:230px">
    <svg class="frame" width="200" height="170"><use href="#pillar-frame"/></svg>
    <svg class="badge" viewBox="0 0 45 45" aria-hidden="true"><use href="#badge-shape"/>
      <g fill="none" stroke="#fff" stroke-width="1"><rect x="12" y="27" width="3" height="5"/><rect x="17" y="24" width="3" height="8"/><rect x="22" y="21" width="3" height="11"/><rect x="27" y="17" width="3" height="15"/><polyline points="12,22 20,15 24,18 32,11"/><circle cx="20" cy="15" r="3"/></g></svg>
    <div class="copy"><h2>Value</h2><p>The project must provide value<br>that significantly exceeds potential<br>project costs and should be aligned<br>with the company's strategy.</p><a class="more" href="#">Read more ›</a></div>
  </article>

  <article class="pillar" style="left:396px;top:230px">
    <svg class="frame" width="200" height="170"><use href="#pillar-frame"/></svg>
    <svg class="badge" viewBox="0 0 45 45" aria-hidden="true"><use href="#badge-shape"/>
      <g fill="none" stroke="#fff" stroke-width="1"><circle cx="16" cy="27" r="4"/><rect x="21" y="20" width="3" height="12"/><rect x="26" y="16" width="3" height="16"/><circle cx="31" cy="22" r="2"/><path d="M28 32 q3-6 6 0"/><polyline points="12,19 19,14 24,16 32,11"/></g></svg>
    <div class="copy"><h2>Capability</h2><p>The company and the<br>implementation team must be<br>capable of implementing the<br>project on their own or with help.</p><a class="more" href="#">Read more ›</a></div>
  </article>

  <article class="pillar" style="left:609px;top:230px">
    <svg class="frame" width="200" height="170"><use href="#pillar-frame"/></svg>
    <svg class="badge" viewBox="0 0 45 45" aria-hidden="true"><use href="#badge-shape"/>
      <g fill="none" stroke="#fff" stroke-width="1"><circle cx="17" cy="20" r="3.5"/><circle cx="27" cy="25" r="3.5"/><circle cx="17" cy="20" r="6" stroke-dasharray="2 2"/><circle cx="27" cy="25" r="6" stroke-dasharray="2 2"/><circle cx="30" cy="14" r="1.5"/><circle cx="22" cy="33" r="1.5"/></g></svg>
    <div class="copy"><h2>Functionality</h2><p>An ERP project must support<br>required business processes, both<br>now and in the future. A systematic<br>review of all business processes<br>and how they will be supported,</p><a class="more" href="#">Read more ›</a></div>
  </article>

  <article class="pillar" style="left:822px;top:230px">
    <svg class="frame" width="200" height="170"><use href="#pillar-frame"/></svg>
    <svg class="badge" viewBox="0 0 45 45" aria-hidden="true"><use href="#badge-shape"/>
      <g fill="none" stroke="#fff" stroke-width="1"><rect x="11" y="12" width="21" height="19"/><line x1="11" y1="16" x2="32" y2="16"/><circle cx="26" cy="25" r="5"/><line x1="30" y1="29" x2="34" y2="33"/><line x1="24" y1="27" x2="24" y2="24"/><line x1="26" y1="27" x2="26" y2="22"/><line x1="28" y1="27" x2="28" y2="25"/></g></svg>
    <div class="copy"><h2>Data</h2><p>ERP systems are data-hungry<br>creatures. Please be careful before<br>assuming that because so much<br>data goes into them, an equal<br>amount of insight will emerge.</p><a class="more" href="#">Read more ›</a></div>
  </article>

  <!-- Row two -->
  <article class="pillar" style="left:182px;top:411px">
    <svg class="frame" width="200" height="170"><use href="#pillar-frame"/></svg>
    <svg class="badge" viewBox="0 0 45 45" aria-hidden="true"><use href="#badge-shape"/>
      <g fill="none" stroke="#fff" stroke-width="1"><circle cx="21" cy="22" r="7"/><circle cx="21" cy="22" r="3"/><line x1="28" y1="17" x2="34" y2="17"/><line x1="28" y1="22" x2="35" y2="22"/><line x1="28" y1="27" x2="34" y2="27"/><line x1="21" y1="11" x2="21" y2="15"/><line x1="21" y1="29" x2="21" y2="33"/><line x1="10" y1="22" x2="14" y2="22"/></g></svg>
    <div class="copy"><h2>Technology</h2><p>What is the platform for the<br>system? Is it offered by a vendor<br>that will be around for as long as<br>your system? Will it integrate with<br>your other systems?</p><a class="more" href="#">Read more ›</a></div>
  </article>

  <article class="pillar" style="left:396px;top:411px">
    <svg class="frame" width="200" height="170"><use href="#pillar-frame"/></svg>
    <svg class="badge" viewBox="0 0 45 45" aria-hidden="true"><use href="#badge-shape"/>
      <g fill="none" stroke="#fff" stroke-width="1"><polyline points="12,32 16,32 16,28 20,28 20,24 24,24 24,20"/><line x1="24" y1="20" x2="24" y2="12"/><polyline points="24,12 29,13.5 24,15"/><circle cx="28" cy="29" r="4"/><circle cx="28" cy="29" r="1.5"/><circle cx="17" cy="19" r="1.8"/></g></svg>
    <div class="copy"><h2>Change Leadership</h2><p>Change leadership (often called<br>change management) considers<br>the human side of an ERP<br>implementation. Change is hard,<br>even if it's a good change.</p><a class="more" href="#">Read more ›</a></div>
  </article>

  <article class="pillar" style="left:609px;top:411px">
    <svg class="frame" width="200" height="170"><use href="#pillar-frame"/></svg>
    <svg class="badge" viewBox="0 0 45 45" aria-hidden="true"><use href="#badge-shape"/>
      <g fill="none" stroke="#fff" stroke-width="1"><circle cx="22.5" cy="19" r="8"/><circle cx="22.5" cy="19" r="5.5"/><polyline points="20,19 22,21 25.5,17"/><polyline points="17,25 14,33 18,31 20,34 22,27"/><polyline points="28,25 31,33 27,31 25,34 23,27"/></g></svg>
    <div class="copy"><h2>Quality</h2><p>Quality is multi-dimensional, and<br>it's more than a measurement; it's<br>a perception. An ERP needs to be<br>reliable.</p><a class="more" href="#">Read more ›</a></div>
  </article>

  <article class="pillar" style="left:822px;top:411px">
    <svg class="frame" width="200" height="170"><use href="#pillar-frame"/></svg>
    <svg class="badge" viewBox="0 0 45 45" aria-hidden="true"><use href="#badge-shape"/>
      <g fill="none" stroke="#fff" stroke-width="1"><circle cx="22.5" cy="17" r="6" stroke-dasharray="2.5 1.5"/><circle cx="22.5" cy="17" r="2.5"/><circle cx="15" cy="26" r="2"/><circle cx="22.5" cy="26" r="2"/><circle cx="30" cy="26" r="2"/><path d="M11 33 q4-6 8 0 M18.5 33 q4-6 8 0 M26 33 q4-6 8 0"/></g></svg>
    <div class="copy"><h2>Governance</h2><p>ERP projects require both<br>management and leadership.<br>Planning, changing plans,<br>communication, decision making,</p><a class="more" href="#">Read more ›</a></div>
  </article>

  <p class="outro">Thanks for watching, I can follow up your branding guidelines</p>
</body>
</html>
```